Pine Arbor Table & Chair Rentals

We need a business card for a table and chair rental company. We rent tables and chairs for weddings, funerals, business events and parties. We want something that looks clean and elegant while not being too busy. We would like colors in the green and blue hues and avoiding anything orange. We want to make sure the font is large enough to be seen easily.

Target Market(s)

Wedding & Event Rentals

Industry/Entity Type

Events

Contact Information for Business Card

Pine Arbor, sales@pinearborrentals.example, pinearborrentals.example, 555-218-0937

Requirements
Must have
• Easy to read font
Should not have
• Orange anywhere in the design

```html
<!DOCTYPE html>
<html lang="en">
<head>
<meta charset="UTF-8">
<title>Pine Arbor Table &amp; Chair Rentals – Business Card</title>
<link rel="stylesheet" href="https://fonts.googleapis.com/css2?family=Exo+2:wght@400;500&display=swap">
<style>
  :root {
    --backdrop: #e4e6e6;
    --card-front: #1f6e73;
    --card-back: #ffffff;
    --ink: #1c3a40;
    --ink-light: #ffffff;
    --rule: #4f6a6e;
    --icon-bg: #1c3a40;
  }
  * { margin: 0; padding: 0; box-sizing: border-box; }
  html, body {
    width: 1189px;
    height: 1200px;
    overflow: hidden;
    background: var(--backdrop);
    font-family: "Exo 2", sans-serif;
  }
  .canvas { position: relative; width: 1189px; height: 1200px; }
  .card {
    position: absolute;
    left: 171px;
    width: 856px;
    height: 488px;
    border-radius: 18px;
    box-shadow: 0 4px 10px rgba(0,0,0,0.18);
  }
  .card--front { top: 68px; background: var(--card-front); color: var(--ink-light); }
  .card--back { top: 626px; background: var(--card-back); color: var(--ink); }

  .brand { position: absolute; }
  .brand__name {
    display: block;
    font-weight: 500;
    line-height: 1;
    white-space: nowrap;
  }
  .brand__tagline {
    display: block;
    font-weight: 400;
    white-space: nowrap;
  }
  .card--front .brand { left: 213px; top: 176px; }
  .card--front .brand__name { font-size: 78px; }
  .card--front .brand__tagline { font-size: 39px; margin-top: 22px; margin-left: 8px; }

  .card--back .brand { left: 48px; top: 190px; }
  .card--back .brand__name { font-size: 52px; }
  .card--back .brand__tagline { font-size: 27px; margin-top: 12px; margin-left: 5px; }

  .divider {
    position: absolute;
    left: 380px;
    top: 64px;
    width: 1px;
    height: 360px;
    background: var(--rule);
  }
  .company {
    position: absolute;
    left: 426px;
    top: 110px;
    font-size: 48px;
    font-weight: 500;
    line-height: 1.2;
  }
  .contacts {
    position: absolute;
    left: 428px;
    top: 250px;
    list-style: none;
  }
  .contacts__item {
    display: flex;
    align-items: center;
    height: 36px;
    font-size: 25px;
    line-height: 1;
  }
  .contacts__icon {
    width: 26px;
    height: 26px;
    margin-right: 12px;
    flex: none;
  }
</style>
</head>
<body>
<main class="canvas">
  <section class="card card--front" aria-label="Card front">
    <div class="brand">
      <span class="brand__name">Pine Arbor</span>
      <span class="brand__tagline">Table and Chair Rentals</span>
    </div>
  </section>

  <section class="card card--back" aria-label="Card back">
    <div class="brand">
      <span class="brand__name">Pine Arbor</span>
      <span class="brand__tagline">Table and Chair Rentals</span>
    </div>
    <div class="divider"></div>
    <h1 class="company">Pine Arbor</h1>
    <ul class="contacts">
      <li class="contacts__item">
        <svg class="contacts__icon" viewBox="0 0 26 26" aria-hidden="true">
          <rect width="26" height="26" rx="5" fill="#1c3a40"/>
          <path d="M9 6c1 0 2 2.5 2 3.3 0 .8-1.3 1.2-1.2 2 .3 1.8 2 3.6 3.8 4 .8.1 1.2-1.2 2-1.2.9 0 3.4 1 3.4 2 0 1.5-1.6 3-3.2 2.8C11 18.4 7.5 14.8 7 10.2 6.8 8 7.8 6 9 6z" fill="#fff"/>
        </svg>
        <span>555-218-0937</span>
      </li>
      <li class="contacts__item">
        <svg class="contacts__icon" viewBox="0 0 26 26" aria-hidden="true">
          <rect width="26" height="26" rx="5" fill="#1c3a40"/>
          <g fill="none" stroke="#fff" stroke-width="1.2">
            <circle cx="13" cy="13" r="8"/>
            <ellipse cx="13" cy="13" rx="3.5" ry="8"/>
            <path d="M5 13h16M6.2 9h13.6M6.2 17h13.6"/>
          </g>
        </svg>
        <span>www.pinearborrentals.example</span>
      </li>
      <li class="contacts__item">
        <svg class="contacts__icon" viewBox="0 0 26 26" aria-hidden="true">
          <rect width="26" height="26" rx="5" fill="#1c3a40"/>
          <g fill="none" stroke="#fff" stroke-width="1.4">
            <rect x="5.5" y="8" width="15" height="10.5"/>
            <path d="M5.5 8l7.5 6 7.5-6M5.5 18.5l5.5-5M20.5 18.5l-5.5-5"/>
          </g>
        </svg>
        <span>sales@pinearborrentals.example</span>
      </li>
    </ul>
  </section>
</main>
</body>
</html>
```